Property Management Company Needs Corporate Marketing Brochure

NEEDED: Corporate marketing brochure for Atlanta-based real estate management company that manages homeowner associations and condominium associations primarily in the Atlanta market. (We don't manage apartments or individual homes for rent.) I've attached our current logo with the current teal and black corporate colors. Also, I've attached an old corporate brochure that gives you some idea of the type of content we use in marketing our services (we no longer use this) .

What I DON'T like about the old corporate brochure:

1.) Too much copy and too few pictures and graphics. People don't read - they skim. How do we capture their attention and convey the sales the message in a few minutes?

2.) Inability to customize easily. We need to be able to make edits to our presentation depending on the client. High rise condo towers have different requirements than single family swim/tennis communities. One thought is to create a "global" corporate brochure that speaks to Harlow's capabilities. In addition to that, create individual sales sheets that address a specific topic (budgets, financials, reserve studies, construction management, case studies, covenant enforcement, for example). I don't know what the format should be so I didn't check anything below.

3.) We haven't done a good job of branding Harlow across a family of materials - i.e., job applications, human resource forms, website, social media, email communication, internal communications, etc. I view this brochure as the first step in creating an overall brand for Harlow. We need someone who can take a global view of our needs and help us create templates for different applications.

Description and message of the brochure:
Harlow Stewardship Group is the best option for community management services in the metro Atlanta region.

Style preferences:
distinctive, clean, memorable, creative - fun?

Color preferences:
corporate logo colors are teal and black against a white background

Industry/Entity Type

Real Estate

```html
<!DOCTYPE html>
<html lang="en">
<head>
<meta charset="utf-8">
<title>Harlow Stewardship Group – Letterhead</title>
<link rel="stylesheet" href="https://fonts.googleapis.com/css2?family=Bebas+Neue&family=Lato:wght@300;700&display=swap">
<style>
  :root {
    --navy: #1c4a79;
    --navy-deep: #163d66;
    --teal: #1fa3b1;
    --body-grey: #7a7a7a;
    --paper: #ffffff;
    --mist: #e9eaec;
    --photo-sky: #c9ced6;
    --photo-city: #6f7f93;
    --photo-trees: #9a6a2c;
    --photo-water: #3a3528;
  }
  * { margin: 0; padding: 0; box-sizing: border-box; }
  html, body { width: 928px; height: 1200px; overflow: hidden; background: var(--paper); }
  .sheet { position: relative; width: 928px; height: 1200px; overflow: hidden; background: var(--paper); }
  .masthead { position: absolute; top: 0; left: 0; width: 928px; height: 300px; }
  .content { position: absolute; top: 348px; left: 54px; width: 816px; }
  .headline {
    font-family: 'Bebas Neue', sans-serif;
    font-weight: 400;
    font-size: 44px;
    letter-spacing: 0.5px;
    color: var(--navy);
    line-height: 1;
    margin-bottom: 22px;
  }
  .body-copy p {
    font-family: 'Lato', sans-serif;
    font-weight: 300;
    font-size: 16.4px;
    line-height: 29.5px;
    color: var(--body-grey);
    text-align: justify;
    margin-bottom: 29px;
  }
  .footer { position: absolute; left: 0; top: 1056px; width: 928px; height: 144px; }
  .footer-band { position: absolute; inset: 0; }
  .contact { position: absolute; left: 20px; top: 64px; font-family: 'Bebas Neue', sans-serif; color: var(--paper); }
  .contact-address { font-size: 20px; letter-spacing: 0.3px; line-height: 1; }
  .contact-web { font-size: 31px; letter-spacing: 0.3px; line-height: 1; margin-top: 4px; }
  .contact-web .accent { color: var(--teal); }
  .brand { position: absolute; left: 596px; top: 50px; display: flex; align-items: center; gap: 16px; }
  .brand-mark { width: 30px; height: 30px; background: var(--navy); }
  .brand-name { font-family: 'Lato', sans-serif; font-weight: 700; font-size: 48px; color: var(--teal); line-height: 1; }
</style>
</head>
<body>
<div class="sheet">
  <svg class="masthead" viewBox="0 0 928 300" xmlns="http://www.w3.org/2000/svg">
    <defs>
      <linearGradient id="photoTone" x1="0" y1="0" x2="0" y2="1">
        <stop offset="0" stop-color="var(--photo-sky)"/>
        <stop offset="0.3" stop-color="var(--photo-city)"/>
        <stop offset="0.6" stop-color="var(--photo-trees)"/>
        <stop offset="1" stop-color="var(--photo-water)"/>
      </linearGradient>
      <linearGradient id="mistBand" x1="0" y1="0" x2="1" y2="0">
        <stop offset="0" stop-color="#ffffff"/>
        <stop offset="1" stop-color="var(--mist)"/>
      </linearGradient>
    </defs>
    <polygon points="0,268 928,178 928,232 0,300" fill="url(#mistBand)"/>
    <polygon role="img" aria-label="City skyline above autumn trees reflected in a park lake" points="0,0 928,0 928,186 0,258" fill="url(#photoTone)"/>
    <polygon points="0,278 442,250 442,262 0,294" fill="var(--navy)"/>
  </svg>

  <main class="content">
    <h1 class="headline">Lorem ipsum dolor sit amet</h1>
    <div class="body-copy">
      <p>&nbsp;Lorem ipsum dolor sit amet, consectetur adipiscing elit. Nam gravida mi et tincidunt rhoncus. Vivamus ullamcorper, dui eu mattis tincidunt, velit leo lobortis tellus, vel blandit odio est eget est. Sed eget scelerisque purus, sed ornare turpis. Suspendisse nisl erat, sollicitudin et mi non, sagittis dapibus lacus. Nulla pellentesque, dolor a pulvinar iaculis, lorem dolor pretium dui, tincidunt malesuada arcu urna sed orci. Sed feugiat dolor nulla, lacinia congue ligula facilisis in. Duis faucibus suscipit enim, in ullamcorper lorem gravida fermentum. Vivamus pretium, metus vitae tempus imperdiet, nisi dui malesuada arcu, nec egestas massa purus non lectus. Suspendisse quis nisi velit.</p>
      <p>Fusce porttitor facilisis sagittis. Nam blandit luctus orci. Nullam pulvinar, velit ac cursus egestas, enim lorem facilisis sem, ut dictum ante ipsum non leo. Nam ut lorem quis ex pulvinar lobortis elementum sed sapien. Nullam in arcu metus. Vestibulum sit amet vestibulum enim, sit amet laoreet massa. Aliquam ullamcorper est in risus semper, id finibus nibh ullamcorper. Nullam quam magna, molestie vitae nisi sed, consectetur mollis mi. Donec porttitor dui at lorem iaculis imperdiet. In hac habitasse platea dictumst. Aliquam leo ante, sagittis nec est id, eleifend placerat odio. Aliquam erat volutpat. In placerat efficitur mi.</p>
      <p>Nullam at tempus arcu. Aliquam vel nisi sed justo pretium scelerisque quis non erat. Integer et enim quis orci rhoncus bibendum a eget nulla. Interdum et malesuada fames ac ante ipsum primis in faucibus. Sed condimentum tristique enim, ut iaculis nisl sollicitudin et. Morbi id scelerisque arcu. Mauris fermentum in erat nec auctor.</p>
    </div>
  </main>

  <footer class="footer">
    <svg class="footer-band" viewBox="0 0 928 144" xmlns="http://www.w3.org/2000/svg">
      <defs>
        <linearGradient id="footerMist" x1="0" y1="0" x2="0" y2="1">
          <stop offset="0" stop-color="#ffffff"/>
          <stop offset="1" stop-color="var(--mist)"/>
        </linearGradient>
        <linearGradient id="footerNavy" x1="0" y1="0" x2="1" y2="1">
          <stop offset="0" stop-color="var(--navy-deep)"/>
          <stop offset="1" stop-color="var(--navy)"/>
        </linearGradient>
      </defs>
      <rect x="0" y="0" width="928" height="144" fill="url(#footerMist)"/>
      <polygon points="0,2 528,2 474,144 0,144" fill="url(#footerNavy)"/>
    </svg>
    <div class="contact">
      <div class="contact-address">2150 Maple Crest Avenue, Suite B#114, Atlanta GA 30341</div>
      <div class="contact-web">www.<span class="accent">Harlow</span>Stewardship<span class="accent">Group</span>.com</div>
    </div>
    <div class="brand">
      <span class="brand-mark"></span>
      <span class="brand-name">Harlow</span>
    </div>
  </footer>
</div>
</body>
</html>
```